Web Design Project

I need designs (PSD only - no programming) for several pages of a new website helping train operators to manage key information about their traindrivers.
The main feature of this website is the management of personnel records (create, edit, search, delete). Another key aspect is the management of user privileges. Since this is a new website we also need a user friendly frontpage, pricing information and how it works sections.
This can be broken down into 9 pages for which we need designs (PSDs).
1. Home
2. Driver record
3. How it works
4. Pricing
5. User administration
6. Help
7. Record list view
8. Login
9. Registration
Navigation (not logged in) are: Home | How it works | Pricing | Customers | About us | Contact
Navigation (logged in) are: Overview | Administration | Manage records | Billing | Help | Contact
Footer: Customer logos | Awards | Terms & Conditions | Privacy
To provide the best support for you to come up with a strong design proposal I will provide DAILY feedback to all participants. We have also created concept mockups (attached) and example pages (below) for each section to give you a clear sense of what we look for.
The core concepts for a successful bid are that the website is EASY to understand, INTUITIVE to navigate, and SIMPLE to use. Most of our users lack technical background and are looking for tool to simplify their work.
The strongest participants (winner and close contenders) will have the opportunity to additional commissioned work on additional sections not included in this brief.
Example Pages (by section)
1. http://www.brovendale.example/site-keepers/
1. http://www.qvt.example/
1. http://www.mondaph.example/
1. http://www.gorvanquest.example/
2. http://www.snapveld.example/profile_edit.gne
3. https://www.tarn.example/how-it-works/
3. http://www.bulkvue.example/learn
4. http://www.pactheron.example/crm/editions-pricing.jsp
4. http://www.brovendale.example/site-keepers/prices
6. https://support.talvora.example/en-gb/
6. http://help.dealmeadow.example/contact_us
8. https://www.careweave.example/uas/login
8. https://www.dealmeadow.example/login
8. http://www.askhollow.example/login/index
For form designs we like Verindo, Bidnook, Snapveld, CareWeave, Chatterly and the concepts presented by Tomas Kerrigan in his classic Layout Craft Shaping the Input Boxes.
For additional guidance see mockups attached!
Target Market(s)
Security, human resources and admin support employees for train operators.
Industry/Entity Type
Learn
Requirements
Should not have
- Home page should not have
Social media icons (chatterly, chirpla, CareWeave, RSS feed)
Contact forms
Read more links
Old trains

```html
<!DOCTYPE html>
<html lang="en">
<head>
<meta charset="utf-8">
<title>RailRoster</title>
<link href="https://fonts.googleapis.com/css2?family=Jost:wght@400;500;700&display=swap" rel="stylesheet">
<style>
:root{
  --bg-dark:#111516;
  --text:#ffffff;
  --accent-red:#d40b0b;
  --nav-active:#ff4a4a;
  --gold:#e0a526;
  --green-top:#86c92c;
  --green-bottom:#4f9a12;
  --blue-top:#3a8fd0;
  --blue-bottom:#1563a6;
  --placeholder:#3c4446;
}
*{box-sizing:border-box;margin:0;padding:0}
html,body{width:1050px;height:1200px;overflow:hidden;background:var(--bg-dark)}
body{font-family:"Jost",sans-serif;color:var(--text);position:relative}
.site-header{position:absolute;left:0;top:0;width:1050px;height:72px;background:linear-gradient(90deg,#16191a,#222a2c 55%,#1b2022);border-bottom:1px solid #0b0d0e}
.brand-box{position:absolute;left:54px;top:17px;width:132px;height:39px;border:1px solid #7b8183;background:#45494a;color:#c7cbcc;font-size:13px;display:flex;align-items:center;justify-content:center}
.main-nav{position:absolute;top:31px;left:0;width:1050px;font-size:14px}
.main-nav a{position:absolute;color:var(--text);text-decoration:none}
.main-nav a.is-active{color:var(--nav-active)}
.hero{position:absolute;top:72px;left:0;width:1050px;height:350px;background:radial-gradient(ellipse at 30% 40%,#2c3a3e 0%,#151b1d 45%,#0b0e0f 100%)}
.hero-image{position:absolute;left:158px;top:74px;width:262px;height:184px;border:1px solid #8a9092;background:linear-gradient(135deg,#4f5759,#3c4345);color:#232829;font-size:21px;display:flex;align-items:center;justify-content:center}
.hero-title{position:absolute;left:506px;top:64px;font-size:46px;font-weight:700;color:var(--accent-red);letter-spacing:-1px;line-height:1.1}
.tagline{position:absolute;left:505px;font-size:21px;color:#151515;background:#fff;padding:0 8px;line-height:29px}
.btn{position:absolute;top:242px;width:140px;height:31px;border-radius:5px;color:#fff;font-size:16px;display:flex;align-items:center;justify-content:center;box-shadow:0 2px 3px rgba(0,0,0,.5)}
.btn-buy{left:510px;background:linear-gradient(var(--green-top),var(--green-bottom))}
.btn-login{left:676px;background:linear-gradient(var(--blue-top),var(--blue-bottom))}
.features{position:absolute;top:422px;left:0;width:1050px;height:526px}
.features-backdrop{position:absolute;inset:0;background:
  radial-gradient(ellipse 45% 25% at 50% 5%,#d9dcdc 0%,rgba(160,165,166,.6) 45%,transparent 100%),
  radial-gradient(ellipse 35% 40% at 90% 55%,#5a2410 0%,rgba(70,30,20,.6) 50%,transparent 100%),
  radial-gradient(ellipse 40% 45% at 20% 40%,#3d4749 0%,transparent 100%),
  linear-gradient(#2a3133,#1a2123)}
.slider-dots{position:absolute;top:10px;left:506px;display:flex;gap:6px}
.slider-dots span{width:8px;height:8px;border-radius:50%;background:#c9c9c9}
.slider-dots span.is-current{background:#b34040}
.feature{position:absolute;width:385px}
.feature h2{font-size:28px;font-weight:700;line-height:1;margin-bottom:24px}
.feature p{font-size:14.4px;line-height:21px;text-align:justify;color:#f2f4f4}
.site-footer{position:absolute;top:948px;left:0;width:1050px;height:252px;background:linear-gradient(90deg,#131819,#1c2324 60%,#2a1a14);border-top:1px solid #0a0c0d}
.footer-heading{position:absolute;top:40px;font-size:16px;color:var(--gold);font-weight:400}
.award-slot{position:absolute;width:211px;height:40px;background:var(--placeholder);opacity:.8}
.footer-links{position:absolute;left:591px;top:72px;list-style:none;font-size:12.5px;line-height:17.5px}
.footer-links a{color:var(--text);text-decoration:none}
.footer-contact{position:absolute;left:766px;top:72px;font-size:12.5px;line-height:17.5px;font-style:normal}
.footer-contact p+p{margin-top:17.5px}
</style>
</head>
<body>
<header class="site-header">
  <div class="brand-box">RailRoster</div>
  <nav class="main-nav">
    <a style="left:591px">How it works</a>
    <a class="is-active" style="left:692px">Pricing</a>
    <a style="left:760px">Customers</a>
    <a style="left:848px">About Us</a>
    <a style="left:929px">Contact</a>
  </nav>
</header>

<section class="hero">
  <div class="hero-image" role="img" aria-label="Product screenshot placeholder">logo/image</div>
  <h1 class="hero-title">RailRoster</h1>
  <div class="tagline" style="top:147px">Helps train operators to manage key information</div>
  <div class="tagline" style="top:179px">about their traindrivers.</div>
  <div class="btn btn-buy">Buy for 99$</div>
  <div class="btn btn-login">Log In</div>
</section>

<section class="features">
  <div class="features-backdrop" role="img" aria-label="Blurred dark photographic backdrop with soft highlights"></div>
  <div class="slider-dots"><span class="is-current"></span><span></span><span></span></div>
  <article class="feature" style="left:74px;top:108px">
    <h2>Clear records</h2>
    <p>With our product, you know exactly what’s going on, how many drivers are availible at the moment, their payment and personal informations.</p>
  </article>
  <article class="feature" style="left:591px;top:108px">
    <h2>Great integration</h2>
    <p>Our API is super easy to use, so you can make you own mobile application, chatterly integration or Panelux 8 Gadget.</p>
  </article>
  <article class="feature" style="left:74px;top:318px">
    <h2>Blazing fast</h2>
    <p>Our product is blazing fast. You don’t have to wait anymore till data are load. They just are. So you can focus on things that really matter - managing drivers not software.</p>
  </article>
  <article class="feature" style="left:591px;top:318px">
    <h2>Beautiful</h2>
    <p>We are delivering stunnig graphics with our product to make your experience as good as possible, so you will love using our app.</p>
  </article>
</section>

<footer class="site-footer">
  <h3 class="footer-heading" style="left:75px">Awards</h3>
  <h3 class="footer-heading" style="left:334px">Customers</h3>
  <h3 class="footer-heading" style="left:591px">Useful links</h3>
  <h3 class="footer-heading" style="left:766px">Contact us</h3>
  <div class="award-slot" style="left:74px;top:79px"></div>
  <div class="award-slot" style="left:74px;top:132px"></div>
  <div class="award-slot" style="left:74px;top:184px"></div>
  <div class="award-slot" style="left:333px;top:79px"></div>
  <div class="award-slot" style="left:333px;top:132px"></div>
  <div class="award-slot" style="left:333px;top:184px"></div>
  <ul class="footer-links">
    <li><a>Pricing</a></li>
    <li><a>How it works</a></li>
    <li><a>About Us</a></li>
    <li><a>Terms &amp; Conditions</a></li>
    <li><a>Privacy</a></li>
  </ul>
  <address class="footer-contact">
    <p>Rue des Lilas Vertes<br>75100 Lorvenne<br>France</p>
    <p>+420 555 010 010<br>contact@railroster.example</p>
    <p>All rights reserved. ©2012</p>
  </address>
</footer>
</body>
</html>
```